Kestowell Chardonnay Wine Label 2024

We need a wine label design for a small, family-owned vineyard in Broke, Hunter Valley of NSW (Australia). The vineyard is called Kestowell and we have an existing logo and 'brand book' for the vineyard home that is rented out for short stay bookings. This is attached and includes font style, colour palette and our Kestowell logo for the accommodation (we're not wedded to this but also probably not after a completely different rethink either as we want the accommodation and the wine to feel part of the same thing.

Project:
The initial label requirement (front and back) is for the Kestowell 2024 Chardonnay, which is called 'Marigold'. The label would need to be able to extend to other varietals (eg Verdehlo and Sparkling) in 2025. Attached is draft copy for front and back for the 2024 Chardonnay as a guide.

STYLE: We like a relatively simple, classic design and have played with both a dark (navy) and a light background (white/cream). Based on the final label design we will order a Tarquo colour to pick up on the label theme.

The Chardonnay bottle dimensions are attached, as is our logo file (if that helps)

Target Market(s)

online 25-50 yearold

Industry/Entity Type

Wine

Requirements
Must have
• front and back label design Kestowell logo and name

```html
<!DOCTYPE html>
<html lang="en">
<head>
<meta charset="utf-8">
<title>Kestowell Marigold 2024 Chardonnay – Front Label</title>
<link href="https://fonts.googleapis.com/css2?family=Crimson+Pro:wght@400&family=Montserrat:wght@400;500;700&display=swap" rel="stylesheet">
<style>
  :root {
    --page-bg: #ffffff;
    --label-cream: #fdf9ee;
    --label-cream-light: #fffdf7;
    --label-band: #f7f0d8;
    --brand-brown: #5a4a3a;
    --wine-navy: #1b2030;
    --vintage-grey: #3a3a3a;
    --varietal-gold: #f2c230;
    --volume-grey: #9a968c;
    --faint-gold: #f3e6b0;
    --script-tone: #e9e1cc;
    --rule-grey: #b8b2a2;
  }

  * { margin: 0; padding: 0; box-sizing: border-box; }

  html, body {
    width: 720px;
    height: 1200px;
    overflow: hidden;
    background: var(--page-bg);
  }

  .canvas {
    position: relative;
    width: 720px;
    height: 1200px;
  }

  .front-label {
    position: absolute;
    left: 40px;
    top: 303px;
    width: 640px;
    height: 593px;
    background:
      linear-gradient(90deg,
        var(--label-cream-light) 0%,
        var(--label-cream) 40%,
        var(--label-band) 48%,
        var(--label-cream) 56%,
        var(--label-cream-light) 100%);
    overflow: hidden;
  }

  .brand-mark {
    position: absolute;
    left: 556px;
    top: 44px;
    width: 30px;
    height: 30px;
    border-radius: 50%;
    background: var(--brand-brown);
  }

  .brand-name {
    position: absolute;
    right: 84px;
    top: 92px;
    font-family: "Crimson Pro", Georgia, serif;
    font-weight: 400;
    font-size: 54px;
    line-height: 1;
    color: var(--brand-brown);
  }

  .faint-motif {
    position: absolute;
    left: 90px;
    top: 200px;
    width: 230px;
    height: 230px;
    border-radius: 50%;
    background: var(--faint-gold);
    opacity: 0.45;
  }

  .wine-title {
    position: absolute;
    right: 64px;
    top: 390px;
    text-align: right;
  }

  .wine-name {
    font-family: "Montserrat", Arial, sans-serif;
    font-weight: 700;
    font-size: 60px;
    line-height: 1;
    letter-spacing: 4px;
    color: var(--wine-navy);
  }

  .wine-detail {
    margin-top: 8px;
    font-family: "Montserrat", Arial, sans-serif;
    font-weight: 500;
    font-size: 17px;
    letter-spacing: 2px;
    color: var(--vintage-grey);
  }

  .wine-detail .varietal {
    color: var(--varietal-gold);
    font-weight: 400;
    letter-spacing: 4px;
  }

  .volume {
    position: absolute;
    left: 38px;
    top: 522px;
    font-family: "Montserrat", Arial, sans-serif;
    font-weight: 400;
    font-size: 14px;
    letter-spacing: 2px;
    color: var(--volume-grey);
  }

  .region-script {
    position: absolute;
    left: 290px;
    top: 500px;
    width: 240px;
    height: 48px;
    background: var(--script-tone);
    border-radius: 4px;
  }

  .region-rule {
    position: absolute;
    left: 290px;
    top: 525px;
    width: 330px;
    height: 6px;
  }
</style>
</head>
<body>
  <main class="canvas">
    <section class="front-label" aria-label="Kestowell Marigold 2024 Chardonnay front label">
      <span class="brand-mark" aria-hidden="true"></span>
      <div class="brand-name">Kestowell</div>

      <div class="faint-motif" aria-hidden="true"></div>

      <div class="wine-title">
        <h1 class="wine-name">MARIGOLD</h1>
        <p class="wine-detail">2024 // <span class="varietal">CHARDONNAY</span></p>
      </div>

      <div class="volume">750ML.</div>

      <div class="region-script" role="img" aria-label="Hand-lettered Hunter Valley region signature"></div>
      <svg class="region-rule" viewBox="0 0 330 6" aria-hidden="true">
        <line x1="40" y1="3" x2="270" y2="3" stroke="var(--rule-grey)" stroke-width="1" stroke-dasharray="3 3"/>
        <line x1="240" y1="2" x2="328" y2="1" stroke="var(--wine-navy)" stroke-width="1.2"/>
      </svg>
    </section>
  </main>
</body>
</html>
```